Im open to ideas.. I was thinking on my business cards aswell as my logo. a place for my name. email. phone number and abn..

ive attched a file with my business logo. which i dont love the colours.. i was think a dark background with charcoal letters so something along those colour schumes but im open to ideas..

Industry/Entity Type

Business

Logo Text

RLB Constructions

```html
<!DOCTYPE html>
<html lang="en">
<head>
<meta charset="utf-8">
<title>Korvane Constructions – Business Card</title>
<link rel="stylesheet" href="https://fonts.googleapis.com/css2?family=Arvo:wght@400;700&family=Roboto:wght@400;700&display=swap">
<style>
  :root {
    --backdrop: #e6e6e4;
    --stone-dark: #1f1f1f;
    --stone-mid: #353535;
    --stone-light: #4a4a48;
    --ink: #ffffff;
    --ink-soft: #e8e8e8;
    --rule: rgba(255, 255, 255, 0.85);
  }
  * { box-sizing: border-box; margin: 0; padding: 0; }
  html, body {
    width: 1200px;
    height: 800px;
    overflow: hidden;
    background: var(--backdrop);
  }
  .canvas {
    width: 1200px;
    height: 800px;
    display: flex;
    align-items: center;
    justify-content: center;
  }
  .business-card {
    position: relative;
    width: 840px;
    height: 480px;
    border-radius: 34px;
    overflow: hidden;
    box-shadow: 0 10px 30px rgba(0, 0, 0, 0.25);
  }
  .stone-surface {
    position: absolute;
    inset: 0;
    background:
      radial-gradient(ellipse at 30% 25%, var(--stone-light) 0%, transparent 55%),
      radial-gradient(ellipse at 75% 70%, var(--stone-mid) 0%, transparent 60%),
      linear-gradient(135deg, var(--stone-mid) 0%, var(--stone-dark) 100%);
  }
  .card-content {
    position: relative;
    height: 100%;
    display: flex;
    flex-direction: column;
    align-items: center;
    padding-top: 100px;
    color: var(--ink);
  }
  .brand-name {
    font-family: "Roboto", sans-serif;
    font-weight: 700;
    font-size: 50px;
    letter-spacing: 3px;
    text-transform: uppercase;
    color: var(--ink);
    line-height: 1;
  }
  .holder-name {
    margin-top: 62px;
    font-family: "Arvo", serif;
    font-size: 30px;
    line-height: 1.2;
    color: var(--ink);
  }
  .rule {
    width: 440px;
    height: 1px;
    background: var(--rule);
  }
  .rule--upper { margin-top: 10px; }
  .rule--lower { margin-top: 14px; }
  .abn {
    margin-top: 10px;
    font-family: "Arvo", serif;
    font-size: 15px;
    letter-spacing: 1px;
    color: var(--ink-soft);
  }
  .contact-line {
    display: flex;
    align-items: center;
    gap: 10px;
    margin-top: 12px;
    font-size: 22px;
    color: var(--ink);
  }
  .contact-line--email { font-family: "Arvo", serif; }
  .contact-line--phone { font-family: "Roboto", sans-serif; font-size: 25px; }
  .contact-icon { width: 22px; height: 22px; flex: none; }
</style>
</head>
<body>
<main class="canvas">
  <article class="business-card">
    <div class="stone-surface" role="img" aria-label="Dark charcoal slate stone texture"></div>
    <div class="card-content">
      <h1 class="brand-name">Korvane Constructions</h1>
      <p class="holder-name">Dale Morgan</p>
      <div class="rule rule--upper"></div>
      <p class="abn">ABN: 51 318 902 467</p>
      <p class="contact-line contact-line--email">
        <svg class="contact-icon" viewBox="0 0 22 22" aria-hidden="true">
          <circle cx="11" cy="11" r="11" fill="#ffffff"/>
          <rect x="5.5" y="7.5" width="11" height="7.5" rx="1" fill="#2a2a2a"/>
          <path d="M5.8 8 L11 12 L16.2 8" fill="none" stroke="#ffffff" stroke-width="1.1"/>
        </svg>
        dale.morgan@korvane.com
      </p>
      <div class="rule rule--lower"></div>
      <p class="contact-line contact-line--phone">
        <svg class="contact-icon" viewBox="0 0 22 22" aria-hidden="true">
          <circle cx="11" cy="11" r="11" fill="#ffffff"/>
          <path d="M7.6 5.6 L9.4 5.3 L10.4 8.2 L9.1 9.3 C9.8 10.9 11.1 12.2 12.7 12.9 L13.8 11.6 L16.7 12.6 L16.4 14.4 C16.2 15.4 15.3 16.1 14.3 16 C9.8 15.5 6.5 12.2 6 7.7 C5.9 6.7 6.6 5.8 7.6 5.6 Z" fill="#2a2a2a"/>
        </svg>
        202-555-0187
      </p>
    </div>
  </article>
</main>
</body>
</html>
```